Business Card Design Project

Refresh of logo attached. Require text underneath to be more ledgible, crisper & cleaner.

Overall, staying with same colour scheme need a brighter, crisper, easily readible business card style.

Industry/Entity Type

Business

```html
<!DOCTYPE html>
<html lang="en">
<head>
<meta charset="utf-8">
<title>NGEA Business Card</title>
<link rel="stylesheet" href="https://fonts.googleapis.com/css2?family=Mulish:wght@400;700&display=swap">
<style>
  :root {
    --backdrop: #cfd3d5;
    --card-light: #ecedee;
    --card-dark: #2b3235;
    --ink: #2a3033;
    --ink-soft: #4a5154;
    --teal: #2f8ea8;
    --on-dark: #eef1f2;
    --rule-light: #8a9194;
    --rule-dark: #9aa3a6;
  }
  * { margin: 0; padding: 0; box-sizing: border-box; }
  html, body { width: 1200px; height: 900px; overflow: hidden; }
  body {
    background: var(--backdrop);
    font-family: "Mulish", "Century Gothic", sans-serif;
    color: var(--ink);
    position: relative;
  }
  .card {
    position: absolute;
    left: 280px;
    width: 640px;
    height: 366px;
    border-radius: 4px;
    box-shadow: 0 10px 28px rgba(0,0,0,0.18);
  }
  .card--front { top: 70px; background: var(--card-light); }
  .card--back  { top: 464px; background: var(--card-dark); }

  .brand {
    position: absolute;
    display: flex;
    align-items: flex-start;
    gap: 16px;
  }
  .brand__square {
    width: 50px;
    height: 50px;
    margin-top: 14px;
    background: var(--teal);
  }
  .brand__lockup { display: flex; flex-direction: column; }
  .brand__name {
    font-weight: 400;
    font-size: 74px;
    letter-spacing: 2px;
    line-height: 1;
  }
  .brand__rule {
    height: 1px;
    margin: 8px 0 7px;
    background: var(--rule-light);
  }
  .brand__descriptor {
    font-size: 13px;
    line-height: 1.3;
    letter-spacing: 0.6px;
    text-transform: uppercase;
    color: var(--teal);
  }
  .card--front .brand { left: 236px; top: 54px; }
  .card--front .brand__name { color: var(--ink); }
  .card--back .brand { left: 50%; top: 50%; transform: translate(-50%, -50%); }
  .card--back .brand__name { color: var(--on-dark); }
  .card--back .brand__rule { background: var(--rule-dark); }

  .holder {
    position: absolute;
    left: 58px;
    top: 206px;
  }
  .holder__name {
    font-weight: 700;
    font-size: 19px;
    color: var(--ink);
  }
  .holder__title {
    margin-top: 3px;
    font-size: 15px;
    color: var(--ink-soft);
  }
  .contact {
    position: absolute;
    left: 302px;
    top: 268px;
    font-size: 15px;
    line-height: 1.55;
    color: var(--ink-soft);
  }
  .contact__label { color: var(--teal); font-weight: 700; }
</style>
</head>
<body>
  <section class="card card--front" aria-label="Business card front">
    <div class="brand">
      <span class="brand__square"></span>
      <div class="brand__lockup">
        <span class="brand__name">NGEA</span>
        <span class="brand__rule"></span>
        <p class="brand__descriptor">National Guild of Certified<br>Estate Advisors</p>
      </div>
    </div>
    <div class="holder">
      <p class="holder__name">Daniel R. Whitford</p>
      <p class="holder__title">Certified Executor Advisor</p>
    </div>
    <div class="contact">
      <p><span class="contact__label">T:</span> (555) 201 4470 <span class="contact__label">M:</span> (555) 318 2096</p>
      <p><span class="contact__label">E:</span> daniel@ngea.ca · www.ngea.ca</p>
    </div>
  </section>

  <section class="card card--back" aria-label="Business card back">
    <div class="brand">
      <span class="brand__square"></span>
      <div class="brand__lockup">
        <span class="brand__name">NGEA</span>
        <span class="brand__rule"></span>
        <p class="brand__descriptor">National Guild of Certified<br>Estate Advisors</p>
      </div>
    </div>
  </section>
</body>
</html>
```